Corlane Homes Website for luxury custom home builder with endless detail

Modern website for luxury custom home builder. Simple and easy for viewers to understand what we do. New company formed by retired custom home builder. Company concept is to simplify the building experience with modern technology and introduce a simple pricing strategy for the client. Website must flow. Prefer page less design or possibly something that is up and coming within the web design community. Two galleries: INTERIOR and EXTERIOR. I would like two click on box's when the website is opened showing the galleries as a centerpiece and would also prefer them to play as a slide show. The page needs to fit the entire screen in size. We would like to use Grey, Black and White or the shade of blue that is in our company logo. I would like to see one of my uploaded photos to be in the background. I would also like a 3rd box that will play some type of animated video describing what we do and what our process is. Hoping this would be more interactive for the viewer than clicking on buttons and navigating around wasting time.

Target Market(s)

affluent buyers ages 30-60 who want to built anything from large estates to downsized luzury homes for the retired crowd.

Industry/Entity Type

Home Builder

Number of Pages Required

1 page

Font styles to use
Sans Serif

Colors
33a6d7
000000
333333
5c5c5c
9d9d9d
d9d9d9

Requirements
Must have
• Logo and name at top of page. I would like a pageless web design that includes two gallery box's (Interior and Exterior photos) side by side on the first page. I would also like a 3rd box that will be a eVideo explaining what we do and how we do it. I want as little text as possible. I would like the background to be of one of my interior photos that will flow best and pop when the page loads.

```html
<!DOCTYPE html>
<html lang="en">
<head>
<meta charset="utf-8">
<title>Corlane Homes</title>
<link href="https://fonts.googleapis.com/css2?family=Cinzel:wght@400;700&family=Open+Sans:wght@400;700&display=swap" rel="stylesheet">
<style>
:root{
  --blue:#33a6d7;
  --deep-blue:#1d6aa8;
  --black:#000000;
  --dark:#333333;
  --mid:#5c5c5c;
  --light-grey:#9d9d9d;
  --pale:#d9d9d9;
  --footer-bg:#f1f1f1;
  --white:#ffffff;
}
*{box-sizing:border-box;margin:0;padding:0}
html,body{width:738px;height:1200px;overflow:hidden;background:var(--white)}
body{position:relative;font-family:"Open Sans",Arial,sans-serif;color:var(--dark)}
.abs{position:absolute}
.hero{left:0;top:0;width:738px;height:403px;
  background:linear-gradient(180deg,#4f86d6 0%,#7fb0e6 30%,#6c9a55 48%,#c9a27e 60%,#2f8fe0 72%,#c7b39a 85%,#b79c80 100%)}
.brand{left:48px;top:12px;display:flex;align-items:center;gap:6px;font-family:"Cinzel",Georgia,serif;color:var(--white);font-size:12px}
.brand-box{width:14px;height:14px;background:var(--white)}
.hero-title{left:0;width:738px;top:84px;text-align:center;font-family:"Cinzel",Georgia,serif;font-size:46px;color:var(--white);letter-spacing:1px}
.arrow{top:186px;width:32px;height:32px;background:rgba(60,60,60,.55);display:flex;align-items:center;justify-content:center}
.section-title{font-family:"Cinzel",Georgia,serif;font-size:32px;color:var(--blue);top:432px}
.section-title .dark{color:var(--dark)}
.frame{top:481px;width:307px;height:187px;background:#d4d4d4;padding:6px}
.frame .photo{width:100%;height:100%}
.interior{background:linear-gradient(135deg,#a9b7b8,#d8d3bf 50%,#8d8a78)}
.exterior{background:linear-gradient(180deg,#6fa3d6 0%,#c9a57e 40%,#6e9a4a 70%,#c8bfb0 100%)}
.welcome{left:47px;top:691px;width:643px;height:250px;background:var(--blue);color:var(--white)}
.welcome h2{position:absolute;left:0;width:100%;top:30px;text-align:center;font-family:"Cinzel",Georgia,serif;font-weight:400;font-size:31px}
.welcome h2 .lead{color:var(--deep-blue)}
.mission{position:absolute;left:44px;top:71px;font-family:"Cinzel",Georgia,serif;font-size:13px}
.points{position:absolute;left:44px;top:93px;list-style:none;font-size:10px;line-height:19.3px}
.points li{display:flex;align-items:center;gap:7px}
.note{position:absolute;left:46px;top:171px;width:430px;font-size:10px;line-height:14px}
.note b{display:block}
.welcome-name{position:absolute;left:492px;top:133px;white-space:nowrap;font-family:"Cinzel",Georgia,serif;font-size:14px;color:var(--white)}
.lower{left:0;top:970px;width:738px;height:191px;background:var(--footer-bg)}
.lower h3{position:absolute;top:20px;font-family:"Cinzel",Georgia,serif;font-weight:400;font-size:20px;color:var(--dark)}
.field{position:absolute;left:48px;width:217px;height:24px;border:1px solid #cfcfcf;background:var(--white);font-size:9px;color:var(--mid);padding:6px 6px}
.login-btn{position:absolute;left:48px;top:120px;width:89px;height:25px;background:var(--blue);color:var(--white);font-size:13px;display:flex;align-items:center;justify-content:center}
.links{position:absolute;left:48px;top:156px;font-size:9.5px;color:var(--mid)}
.links span{color:var(--blue)}
.divider{position:absolute;left:369px;top:20px;width:1px;height:145px;background:var(--pale)}
.icon-circle{position:absolute;left:444px;width:42px;height:42px;border-radius:50%;background:var(--white);display:flex;align-items:center;justify-content:center}
.contact-text{position:absolute;font-size:9.5px;line-height:20px;color:var(--dark)}
.bottom-bar{left:0;top:1161px;width:738px;height:39px;background:var(--blue);text-align:center;font-family:"Cinzel",Georgia,serif;font-size:8px;color:var(--white);line-height:39px}
.bottom-bar .name{color:var(--dark)}
</style>
</head>
<body>
  <div class="abs hero" role="img" aria-label="Backyard with pool, arched poolhouse and lounge chairs"></div>
  <div class="abs brand"><span class="brand-box"></span>Corlane Homes</div>
  <h1 class="abs hero-title" style="font-weight:400">CORLANE HOMES</h1>
  <div class="abs arrow" style="left:0"><svg width="10" height="14"><path d="M7 2 2 7l5 5" stroke="#fff" stroke-width="1.5" fill="none"/></svg></div>
  <div class="abs arrow" style="right:0;width:30px"><svg width="10" height="14"><path d="M3 2l5 5-5 5" stroke="#fff" stroke-width="1.5" fill="none"/></svg></div>

  <h2 class="abs section-title" style="left:50px;font-weight:400">Gallery</h2>
  <h2 class="abs section-title" style="left:385px;font-weight:400">ABOUT <span class="dark">US</span></h2>

  <div class="abs frame" style="left:50px">
    <div class="photo interior" role="img" aria-label="Interior living room with sofas and fireplace"></div>
    <svg class="abs" style="left:107px;top:84px" width="70" height="32">
      <rect width="32" height="32" fill="#fff"/>
      <rect x="10" y="10" width="12" height="12" fill="none" stroke="#33a6d7" stroke-width="1.5"/>
      <path d="M7 11V7h4M21 7h4v4M25 21v4h-4M11 25H7v-4" stroke="#33a6d7" stroke-width="1.5" fill="none"/>
      <rect x="38" width="32" height="32" fill="#33a6d7"/>
      <path d="M49 9l12 7-12 7z" fill="#fff"/>
    </svg>
  </div>
  <div class="abs frame" style="left:383px">
    <div class="photo exterior" role="img" aria-label="Home exterior with flowering shrubs and stone landscaping"></div>
    <svg class="abs" style="left:139px;top:77px" width="32" height="32">
      <circle cx="16" cy="16" r="16" fill="#fff"/>
      <path d="M13 10l9 6-9 6z" fill="#33a6d7"/>
    </svg>
  </div>

  <section class="abs welcome">
    <h2><span class="lead">Welcome to</span> Corlane Homes</h2>
    <p class="mission">Our mission is simple:</p>
    <ul class="points">
      <li><svg width="12" height="10"><path d="M6 0 0 5h2v5h3V7h2v3h3V5h2z" fill="#fff"/></svg>Simplify the building experience through modern technology</li>
      <li><svg width="12" height="10"><path d="M6 0 0 5h2v5h3V7h2v3h3V5h2z" fill="#fff"/></svg>Simplify pricing with our simplified pricing strategy</li>
      <li><svg width="12" height="10"><path d="M6 0 0 5h2v5h3V7h2v3h3V5h2z" fill="#fff"/></svg>Craft high quality homes with endless detail</li>
      <li><svg width="12" height="10"><path d="M6 0 0 5h2v5h3V7h2v3h3V5h2z" fill="#fff"/></svg>Have fun! We truly want this experience to be both fun and rewarding for all involved.</li>
    </ul>
    <p class="note">I am blessed to be able to share my passion and make a living at the same time. Thank you for your interest and I hope to see you soon!<b>- Elliot R. Brandell</b></p>
    <div class="welcome-name">Corlane Homes</div>
  </section>

  <section class="abs lower">
    <h3 style="left:49px">Client Login</h3>
    <div class="field" style="top:56px">Enter Email</div>
    <div class="field" style="top:88px">Enter Password</div>
    <div class="login-btn">LOGIN</div>
    <p class="links">Forget Password &nbsp;|&nbsp; <span>Register</span></p>
    <div class="divider"></div>
    <h3 style="left:453px">Contact Info</h3>
    <div class="icon-circle" style="top:53px">
      <svg width="20" height="22"><rect x="9" y="0" width="2.5" height="22" fill="#33a6d7"/><rect x="1" y="4" width="18" height="4" fill="#33a6d7"/><rect x="1" y="11" width="18" height="4" fill="#33a6d7"/></svg>
    </div>
    <p class="contact-text" style="left:504px;top:53px">254, Office area name,<br>City, State, Country</p>
    <div class="icon-circle" style="top:117px">
      <svg width="18" height="18"><path d="M4 1c1 0 2 3 2 4s-1.5 1.5-1 2.5 3 3.5 4 4 1.5-1 2.5-1 4 1 4 2-1.5 3-3 3C7 15.5 2.5 11 1.5 4.5 1.5 3 3 1 4 1z" fill="#33a6d7"/></svg>
    </div>
    <p class="contact-text" style="left:495px;top:117px">Phone No. : + 123 456 7890<br>Email : info@corlanehomes.com</p>
  </section>

  <footer class="abs bottom-bar">© <span class="name">CORLANE HOMES</span> - 2015. All Rights Reserved.</footer>
</body>
</html>
```